Local Restaurant Needs a One Page Breakfast Menu

I own a restaurant and we are going to be starting a new breakfast service. I want a one page menu that is clean, bright, and tongue in cheek. We will only have a limited menu, so there should be plenty of space to work with. I will not want actual food pictures, but more of a cartoon style representations of food. I'd like a modern cartoon style mixed with our current 1950s theme.

Name of Restaurant: Pellby's
Location: 2493 W. Larch. Hutchinson, KS 58214 - Phone: 620-555-3047 (including location is not a requirement)

Breakfast Hours: 6:30 am - 10:30 am

The two colors selected below are not required, but they are the two colors that are featured inside the dining room of the restaurant.

Industry/Entity Type

Restaurant

Colors
8667ad
acd036

Requirements
Must have
• Menu must only be one page (either standard letter or oversized - either would be ok).

Menu items:

Stuffed Omellete. Stuffing choices: cheese, peppers, jalapenos, onions, tomatoes, salsa, sour cream, green onions, sausage, bacon, ham

Pellby's Blintz (thin, stuffed, pancakes): Stuffing choices: chocolate chips, Q&Zs, Talbot's Nibbles, strawberries, blueberries, raspberries, bananas, sour cream

Homemade Coffee Cake

Cinnamon Rolls

Beverages - Coffee, Soda, Milk

Prices not set (use placeholders).

```html
<!DOCTYPE html>
<html lang="en">
<head>
<meta charset="utf-8">
<title>Pellby's Breakfast Menu</title>
<link rel="stylesheet" href="https://fonts.googleapis.com/css2?family=Open+Sans:wght@400;500;600;700&display=swap">
<style>
  :root {
    --purple-deep: #33195e;
    --purple-mid: #8667ad;
    --lavender: #b9a0dc;
    --lavender-pale: #e3d8f3;
    --paper: #ffffff;
    --lime: #acd036;
    --name-red: #e0242a;
    --ribbon: #3f3f3f;
    --ribbon-tail: #2a2a2a;
    --ink: #5a5a5a;
    --ink-soft: #6a6a6a;
    --leader: #b8b8b8;
    --hours: #d2d2d2;
  }
  * { box-sizing: border-box; margin: 0; padding: 0; }
  html, body {
    width: 927px; height: 1200px; overflow: hidden; background: var(--paper);
  }
  .menu {
    position: relative; width: 927px; height: 1200px; overflow: hidden;
    font-family: "Open Sans", Arial, sans-serif; color: var(--ink);
  }
  .menu__border {
    position: absolute; inset: 0; background: var(--purple-deep); overflow: hidden;
  }
  .menu__border::before {
    content: ""; position: absolute; left: 22px; right: 26px; top: 18px; bottom: 28px;
    background: linear-gradient(180deg, var(--lavender) 0%, var(--lavender-pale) 50%, var(--lavender) 100%);
    filter: blur(4px);
  }
  .menu__border::after {
    content: ""; position: absolute; left: 95px; right: 95px; top: 100px; bottom: 120px;
    background: var(--paper); filter: blur(30px);
  }
  .menu__frame-lines { position: absolute; inset: 0; }
  .brand {
    position: absolute; left: 275px; top: 8px; width: 378px; height: 378px;
    border-radius: 50%; background: var(--lime);
  }
  .brand__name {
    position: absolute; top: 122px; left: 0; width: 100%; text-align: center;
    font-size: 78px; font-weight: 700; color: var(--name-red); line-height: 1;
  }
  .ribbon { position: absolute; left: 193px; top: 240px; width: 542px; height: 125px; }
  .ribbon__text {
    position: absolute; left: 260px; top: 254px; width: 408px; text-align: center; color: #fff;
  }
  .ribbon__title { font-size: 44px; line-height: 56px; }
  .ribbon__hours { font-size: 23px; line-height: 30px; color: var(--hours); }
  .items { position: absolute; left: 131px; top: 420px; width: 677px; }
  .item__head { display: flex; align-items: baseline; font-size: 25px; line-height: 40px; }
  .item__name { color: var(--ink-soft); white-space: nowrap; }
  .item--featured .item__name { font-weight: 500; color: var(--ink); }
  .item__leader {
    flex: 1; margin: 0 12px; border-bottom: 3px dotted var(--leader); transform: translateY(-5px);
  }
  .item__price { font-weight: 600; color: var(--ink); }
  .item__desc { width: 590px; font-size: 18.5px; line-height: 36px; color: var(--ink-soft); }
  .item__label { text-decoration: underline; }
  .item--omelette { margin-bottom: 34px; }
  .item--blintz { margin-bottom: 35px; }
  .item--compact { margin-bottom: 33px; }
  .item--compact .item__name { font-size: 26px; }
  .item--beverages .item__name { font-size: 26px; }
</style>
</head>
<body>
<main class="menu">
  <div class="menu__border" role="img" aria-label="Hand-painted purple grunge border with paint splatters"></div>
  <svg class="menu__frame-lines" width="927" height="1200" viewBox="0 0 927 1200" aria-hidden="true">
    <g fill="none" stroke="#4a2d7c" stroke-width="1.5" opacity="0.8">
      <line x1="82" y1="108" x2="822" y2="62"/>
      <line x1="118" y1="162" x2="108" y2="1045"/>
      <line x1="792" y1="80" x2="832" y2="1082"/>
      <line x1="92" y1="1092" x2="812" y2="1060"/>
      <line x1="300" y1="1130" x2="840" y2="1115"/>
    </g>
  </svg>

  <div class="brand">
    <div class="brand__name">Pellby's</div>
  </div>

  <svg class="ribbon" viewBox="0 0 542 125" aria-hidden="true">
    <polygon points="0,8 90,8 90,118 0,118 28,63" fill="var(--ribbon-tail)"/>
    <polygon points="542,8 452,8 452,118 542,118 514,63" fill="var(--ribbon-tail)"/>
    <rect x="67" y="10" width="408" height="108" fill="var(--ribbon)"/>
    <line x1="75" y1="20" x2="467" y2="20" stroke="#9a9a9a" stroke-width="2" stroke-dasharray="2 4"/>
    <line x1="75" y1="108" x2="467" y2="108" stroke="#9a9a9a" stroke-width="2" stroke-dasharray="2 4"/>
  </svg>
  <div class="ribbon__text">
    <div class="ribbon__title">Breakfast Menu</div>
    <div class="ribbon__hours">6:30 am - 10:30 am</div>
  </div>

  <section class="items">
    <article class="item item--featured item--omelette">
      <div class="item__head"><span class="item__name">Stuffed Omellete</span><span class="item__leader"></span><span class="item__price">$0.00</span></div>
      <p class="item__desc"><span class="item__label">Stuffing choices</span>: cheese, peppers, jalapenos, onions, tomatoes, salsa, sour cream, green onions, sausage, bacon, ham</p>
    </article>
    <article class="item item--featured item--blintz">
      <div class="item__head"><span class="item__name">Pellby's Blintz (thin, stuffed, pancakes)</span><span class="item__leader"></span><span class="item__price">$0.00</span></div>
      <p class="item__desc"><span class="item__label">Stuffing choices</span>: chocolate chips, Q&amp;Zs, Talbot's Nibbles, strawberries, blueberries, raspberries, bananas, sour cream</p>
    </article>
    <article class="item item--compact">
      <div class="item__head"><span class="item__name">Homemade Coffee Cake</span><span class="item__leader"></span><span class="item__price">$0.00</span></div>
    </article>
    <article class="item item--compact">
      <div class="item__head"><span class="item__name">Cinnamon Rolls</span><span class="item__leader"></span><span class="item__price">$0.00</span></div>
    </article>
    <article class="item item--beverages">
      <div class="item__head"><span class="item__name">Beverages</span><span class="item__leader"></span><span class="item__price">$0.00</span></div>
      <p class="item__desc">Coffee, Soda, Milk</p>
    </article>
  </section>
</main>
</body>
</html>
```